依頼詳細
ラックに並べられた時に見えるよう(雑誌のように)タイトルは上部にお願いします。写真を大きめに使ってください。美しい音で心に深くしみわたるような演奏にしたいと思っています。やさしく透明感のあるイメージでお願いします。
記載項目
森川沙織ピアノリサイタル
2014年11月8日(土)/開演18:00(開場17:30)
ソラノ心斎橋音楽サロン゛Brise”(大阪駅前第3ビル1F)
入場料(全自由席)前売:3000円 当日3500円 *未就学児の入場はごご遠慮くださいチケット販売 t* ティーナビ(サンデイストア Sunaターミナル)
お問い合わせ ソラノ心斎橋 大阪市北区曽根崎4丁目7番2(大阪駅前第3ビル1F)Tel. 06-6921-4057 , http://saorimori-piano.example/
後援 浪華音楽学院同窓会《響友会》、近畿鍵盤文化協会/
Program (原語表記のものを添付させていただきました)
モーツァルト/ソナタ第10番ハ長調 K.330
ラヴェル/ソナチネ
ラヴェル/「鏡」より 道化師の朝の歌
シューマン/交響的練習曲Op.13
Profile (添付させていただきました)
サイズ
A4
ページ数
片面
希望イメージ
シンプル 複雑
単色 カラフル
暗い 明るい
日常 高級
遊び心 厳粛
未来的 伝統的
女性的 男性的
希望する色
設定なし
納品ファイル
• イラストレーター形式 (.ai)
• フォトショップ形式 (.psd)
補足説明
写真を3枚添付していますが、どれか1枚を選んで使ってください。写真はイメージに合うようにカットしたり加工してくださって結構です。プログラムも添付しましたが、原語表記なしの日本語表記のみでも結構です。ナチュラルなイメージが希望です。
写真をもう一度添付してみました。
たびたび申し訳ありません。
プロフィール、並びに プログラムのファイルも添付できていなかったようなので、そちらももう一度添付します。
よろしくお願いいたします。
数々のご提案ありがとうございます。
みなさんとてもステキなのですが、私の好みを補足させていただきます。

顔以外のスペースが文字で埋まってしまうのは好きではありません。
「間」というのか、「抜け感」というのでしょうか…適度なスペースがほしいです。
音楽も「音と音のあいだに音楽が存在する」ものです。
こんな写真で申し訳ありませんが、ぜひアーティストとしてのセンス、インスピレーションを発揮してください☆よろしくお願いいたします。
■ 選んだ理由

私が表現したい音のイメージと合っているように思いました。
光のキラキラとしたようなものが入っていて、それが音のキラキラに通じるように思ったのと、透明感が感じられ、また柔らかい雰囲気もあると思います。
それなのに、チラシを見たときの印象が強いので、この提案に決めました。

■ 提案者全員のお礼・コメント

たくさんのご提案ありがとうございました。みなさんとてもステキなので、当選&次点を選ぶのが失礼なくらいでした。自分で考えるようなものとは全く違って、さすがプロのお仕事だなぁと思いました。多くのワガママを聞き入れてくださり、本当にありがとうございました。またお願いしたいと思います。感謝申し上げます。

```html
<!DOCTYPE html>
<html lang="ja">
<head>
<meta charset="utf-8">
<title>森川沙織 ピアノリサイタル</title>
<link rel="stylesheet" href="https://fonts.googleapis.com/css2?family=Noto+Serif+JP:wght@300;400;600&family=Noto+Sans+JP:wght@400;500&family=Parisienne&family=Cormorant+Garamond:ital,wght@1,400&display=swap">
<style>
  :root {
    --rose-light: #e4b9cc;
    --rose: #cf8fad;
    --rose-deep: #b86e92;
    --ink: #6e4c5c;
    --ink-soft: #8a6a78;
    --paper: #fbf2f6;
  }
  html, body { margin: 0; padding: 0; overflow: hidden; background: #fff; }
  .flyer {
    position: relative;
    width: 849px; height: 1200px;
    overflow: hidden;
    background: var(--paper);
    font-family: "Noto Serif JP", serif;
    color: var(--ink);
  }
  .portrait {
    position: absolute; inset: 0;
    background:
      radial-gradient(ellipse 330px 430px at 250px 560px, #e9c6b8 0%, #f1d6d6 45%, rgba(248,230,238,0) 75%),
      radial-gradient(ellipse 260px 300px at 520px 260px, #ffffff 0%, rgba(255,255,255,0) 70%),
      linear-gradient(180deg, #f7e6ee 0%, #f3dbe6 40%, #f8eaf0 70%, #fdf7fa 100%);
  }
  .portrait::after {
    content: ""; position: absolute; left: 0; top: 820px; width: 849px; height: 380px;
    background: linear-gradient(180deg, rgba(253,247,250,0) 0%, rgba(253,247,250,.9) 45%, #fdf7fa 100%);
  }
  .title { position: absolute; left: 0; top: 0; width: 849px; }
  .title-name {
    position: absolute; left: 40px; top: 22px;
    font-weight: 300; font-size: 118px; letter-spacing: 72px;
    color: var(--rose-light); line-height: 1;
  }
  .title-roman {
    position: absolute; font-family: "Cormorant Garamond", serif; font-style: italic;
    font-size: 20px; color: var(--rose);
  }
  .title-roman.family { left: 300px; top: 24px; }
  .title-roman.given { left: 720px; top: 24px; }
  .title-sub {
    position: absolute; right: 34px; top: 178px;
    font-size: 52px; font-weight: 400; letter-spacing: 6px; color: var(--rose);
  }
  .program { position: absolute; left: 500px; top: 405px; width: 330px; }
  .program h2 {
    margin: 0 0 6px; font-family: "Parisienne", cursive; font-weight: 400;
    font-size: 34px; color: var(--rose-deep);
  }
  .program ul { list-style: none; margin: 0; padding: 0; }
  .program li { margin-bottom: 9px; font-size: 15px; line-height: 1.35; color: var(--ink); }
  .program li::before { content: "♬"; color: var(--rose); margin-right: 4px; }
  .program .orig {
    display: block; padding-left: 18px;
    font-family: "Cormorant Garamond", serif; font-style: italic; font-size: 13px; color: var(--ink-soft);
  }
  .date { position: absolute; left: 520px; top: 728px; width: 310px; }
  .date-year { position: absolute; left: 0; top: 48px; font-size: 26px; letter-spacing: 4px; color: var(--rose-deep); }
  .date-day { position: absolute; left: 68px; top: 0; font-size: 86px; font-weight: 300; color: var(--rose-deep); line-height: 1; }
  .date-week {
    position: absolute; left: 262px; top: 42px; width: 38px; height: 38px; border-radius: 50%;
    border: 1.5px solid var(--rose); color: var(--rose-deep); font-size: 20px;
    display: flex; align-items: center; justify-content: center;
  }
  .date-time { position: absolute; left: 70px; top: 100px; font-size: 15px; color: var(--ink); }
  .venue { position: absolute; right: 30px; top: 862px; text-align: right; color: var(--ink); }
  .venue-name { font-size: 19px; letter-spacing: 1px; }
  .venue-name b { font-family: "Cormorant Garamond", serif; font-style: italic; font-weight: 400; font-size: 30px; color: var(--rose-deep); margin-left: 6px; }
  .venue-note { font-size: 12px; color: var(--ink-soft); }
  .rule { position: absolute; left: 36px; top: 940px; width: 777px; height: 1px; background: var(--rose-light); }
  .info { position: absolute; left: 40px; top: 952px; width: 770px; font-family: "Noto Sans JP", sans-serif; font-size: 13px; line-height: 1.7; color: var(--ink); }
  .info dl { margin: 0; display: grid; grid-template-columns: 100px 1fr; }
  .info dt { color: var(--rose-deep); font-weight: 500; }
  .info dd { margin: 0; }
  .profile { position: absolute; left: 40px; top: 1068px; width: 420px; font-family: "Noto Sans JP", sans-serif; }
  .profile h3 { margin: 0 0 4px; font-family: "Parisienne", cursive; font-weight: 400; font-size: 24px; color: var(--rose-deep); }
  .profile h3 span { font-family: "Noto Serif JP", serif; font-size: 13px; color: var(--ink); margin-left: 8px; }
  .profile p { margin: 0; font-size: 10.5px; line-height: 1.65; color: var(--ink-soft); }
  .support { position: absolute; right: 36px; top: 1150px; width: 330px; font-family: "Noto Sans JP", sans-serif; font-size: 11.5px; line-height: 1.6; color: var(--ink); }
  .support dt { color: var(--rose-deep); float: left; margin-right: 8px; }
  .support dd { margin: 0; }
</style>
</head>
<body>
<main class="flyer">
  <div class="portrait" role="img" aria-label="Soft, bright portrait of the smiling pianist in a pink dress, set in a light-filled hall with sparkling pink highlights"></div>

  <header class="title">
    <h1 class="title-name">森川沙織</h1>
    <span class="title-roman family">Morikawa</span>
    <span class="title-roman given">Saori</span>
    <p class="title-sub">ピアノリサイタル</p>
  </header>

  <section class="program">
    <h2>Program</h2>
    <ul>
      <li>モーツァルト／ソナタ第10番ハ長調 K.330<span class="orig">W. A. Mozart / Sonata No.10 C-dur K.330</span></li>
      <li>ラヴェル／ソナチネ<span class="orig">M. Ravel / Sonatine</span></li>
      <li>ラヴェル／「鏡」より 道化師の朝の歌<span class="orig">M. Ravel / Miroirs “Alborada del gracioso”</span></li>
      <li>シューマン／交響的練習曲 Op.13<span class="orig">R. Schumann / Symphonic Etudes Op.13</span></li>
    </ul>
  </section>

  <section class="date">
    <span class="date-year">2014</span>
    <span class="date-day">11/8</span>
    <span class="date-week">土</span>
    <span class="date-time">開演 18:00（開場 17:30）</span>
  </section>

  <section class="venue">
    <div class="venue-name">ソラノ心斎橋音楽サロン<b>Brise</b></div>
    <div class="venue-note">（浪速中央第5ビル 1F）</div>
  </section>

  <div class="rule"></div>

  <section class="info">
    <dl>
      <dt>入場料</dt><dd>【全自由席】前売：3,000円　当日：3,500円　※未就学児の入場はご遠慮ください</dd>
      <dt>チケット販売</dt><dd>t* ティーナビ（サンデイストア Sunaターミナル）</dd>
      <dt>お問い合わせ</dt><dd>ソラノ心斎橋　大阪市北区曽根崎4丁目7番2（浪速中央第5ビル 1F）<br>TEL. 06-6921-4057　http://saorimori-piano.example/</dd>
    </dl>
  </section>

  <section class="profile">
    <h3>Profile<span>森川 沙織</span></h3>
    <p>浪華音楽学院ピアノ科卒業。在学中より室内楽や伴奏に親しみ、卒業後は関西を中心にソロリサイタルを重ねる。現在は後進の指導にも力を注ぎ、各地のコンクール審査員を務める。透明な音色と繊細な表現に定評がある。</p>
  </section>

  <dl class="support">
    <dt>後援</dt>
    <dd>浪華音楽学院同窓会《響友会》、近畿鍵盤文化協会</dd>
  </dl>
</main>
</body>
</html>
```